Brivane - Business Cards for a new venture

create business card for a startup classified business dealing in construction materials, the cards need to have a professional look but modern, more serious than playful, one of the samples must include the official font (attached), please explore using the official colors in the company's logo

Target Market(s)

Energy sector

Contact Information for Business Card

Font styles to use
Other font styles liked:
• suissnord

Requirements
Must have
• corporate colors (in logo attached)
Nice to have
• Official font (in one of the samples) font is : suissnord
Should not have
• Cartoonish look

```html
<!DOCTYPE html>
<html lang="en">
<head>
<meta charset="utf-8">
<title>Brivane – Business Cards</title>
<link href="https://fonts.googleapis.com/css2?family=Michroma&display=swap" rel="stylesheet">
<style>
  :root {
    --navy: #134674;
    --grey: #929396;
    --white: #ffffff;
    --edge: #3a3a3a;
  }
  html, body {
    margin: 0;
    padding: 0;
    overflow: hidden;
    background: var(--white);
  }
  .canvas {
    position: relative;
    width: 1200px;
    height: 1200px;
    background: var(--white);
    font-family: "Michroma", sans-serif;
  }
  .card {
    position: absolute;
    box-sizing: border-box;
    border: 1px solid var(--edge);
    background: var(--white);
    overflow: hidden;
  }
  .card--front {
    left: 78px;
    top: 78px;
    width: 841px;
    height: 480px;
  }
  .card--back {
    left: 280px;
    top: 641px;
    width: 842px;
    height: 481px;
  }

  /* Front */
  .brand {
    position: absolute;
    left: 0;
    right: 0;
    top: 50%;
    transform: translateY(-50%);
    display: flex;
    align-items: center;
    justify-content: center;
    gap: 22px;
  }
  .brand__mark {
    width: 22px;
    height: 22px;
    background: var(--navy);
  }
  .brand__name {
    color: var(--grey);
    font-size: 38px;
    letter-spacing: 6px;
    text-transform: uppercase;
  }

  /* Back */
  .back__panel {
    position: absolute;
    inset: 0;
    width: 100%;
    height: 100%;
  }
  .holder {
    position: absolute;
    left: 80px;
    top: 95px;
    width: 300px;
    text-align: center;
    color: var(--navy);
  }
  .holder__name {
    font-size: 28px;
    line-height: 36px;
    letter-spacing: 3px;
  }
  .holder__role {
    font-size: 22px;
    line-height: 34px;
    letter-spacing: 4px;
  }
  .contact {
    position: absolute;
    display: flex;
    align-items: center;
    gap: 14px;
    color: var(--white);
    font-size: 17px;
    letter-spacing: 2px;
    text-transform: uppercase;
    white-space: nowrap;
    transform: translateY(-50%);
  }
  .contact__icon {
    width: 24px;
    height: 24px;
    flex: none;
  }
  .contact--mobile { left: 354px; top: 335px; }
  .contact--phone { left: 324px; top: 370px; }
  .contact--email { left: 294px; top: 404px; }
  .contact--address { left: 262px; top: 439px; }
</style>
</head>
<body>
<div class="canvas">

  <section class="card card--front">
    <div class="brand">
      <span class="brand__mark"></span>
      <span class="brand__name">Brivane</span>
    </div>
  </section>

  <section class="card card--back">
    <svg class="back__panel" viewBox="0 0 842 481" preserveAspectRatio="none" aria-hidden="true">
      <polygon points="730,0 842,0 842,481 162,481" fill="var(--navy)"/>
    </svg>

    <div class="holder">
      <div class="holder__name">Name</div>
      <div class="holder__role">Designation</div>
    </div>

    <div class="contact contact--mobile">
      <svg class="contact__icon" viewBox="0 0 24 24" aria-hidden="true">
        <circle cx="12" cy="12" r="11" fill="none" stroke="#fff" stroke-width="1.5"/>
        <rect x="8.5" y="5.5" width="7" height="13" rx="1.2" fill="none" stroke="#fff" stroke-width="1.4"/>
        <circle cx="12" cy="16" r="0.9" fill="#fff"/>
      </svg>
      <span>0450 281736</span>
    </div>

    <div class="contact contact--phone">
      <svg class="contact__icon" viewBox="0 0 24 24" aria-hidden="true">
        <circle cx="12" cy="12" r="11" fill="none" stroke="#fff" stroke-width="1.5"/>
        <path d="M8 6.5c-1 .6-1.6 1.6-1.2 3 .9 3.4 3.8 6.4 7.3 7.5 1.3.4 2.4-.2 3-1.2l-2.2-1.8-1.4 1c-1.8-.8-3.2-2.3-3.9-4l1-1.4z" fill="#fff"/>
      </svg>
      <span>905 31862047</span>
    </div>

    <div class="contact contact--email">
      <svg class="contact__icon" viewBox="0 0 24 24" aria-hidden="true">
        <circle cx="12" cy="12" r="11" fill="none" stroke="#fff" stroke-width="1.5"/>
        <rect x="6" y="8" width="12" height="8.5" fill="#fff"/>
        <path d="M6 8l6 5 6-5" fill="none" stroke="var(--navy)" stroke-width="1.2"/>
      </svg>
      <span>@brivane.com</span>
    </div>

    <div class="contact contact--address">
      <svg class="contact__icon" viewBox="0 0 24 24" aria-hidden="true">
        <circle cx="12" cy="12" r="11" fill="none" stroke="#fff" stroke-width="1.5"/>
        <path d="M12 19s-5-5-5-8.5a5 5 0 0 1 10 0C17 14 12 19 12 19z" fill="#fff"/>
        <circle cx="12" cy="10.5" r="1.8" fill="var(--navy)"/>
      </svg>
      <span>Address</span>
    </div>
  </section>

</div>
</body>
</html>
```